Business Card Design

We need a design for business cards for our company. We have a logo. We teach EMT's and we are based out of Virginia. The information that will need to add would be, name, title, phone number, email, address. On the back of the business card would be "We help you, help others"

Target Market(s)

People that want to become EMT's

Colors

Designer to choose colors to be used in the design.

Requirements
Must have
• company logo

```html
<!DOCTYPE html>
<html lang="en">
<head>
<meta charset="UTF-8">
<title>Rescue Ready Academy – Business Card</title>
<link rel="stylesheet" href="https://fonts.googleapis.com/css2?family=Varela+Round&display=swap">
<style>
  :root {
    --frame-red: #e8202a;
    --sheet: #ffffff;
    --card: #222b35;
    --ink: #ffffff;
    --brand-red: #e0213a;
  }
  * { box-sizing: border-box; margin: 0; padding: 0; }
  html, body { width: 982px; height: 1200px; overflow: hidden; }
  body {
    position: relative;
    background: var(--sheet);
    font-family: "Varela Round", sans-serif;
    color: var(--ink);
  }
  .sheet-frame {
    position: absolute; inset: 0;
    border: 7px solid var(--frame-red);
  }
  .card {
    position: absolute;
    left: 100px; width: 783px;
    background: var(--card);
  }
  .card--front { top: 73px; height: 497px; }
  .card--back { top: 623px; height: 502px; }

  .brand {
    position: absolute;
    display: flex; align-items: center; gap: 10px;
    color: var(--brand-red);
    white-space: nowrap;
    transform: translateX(-50%);
  }
  .brand__dot {
    width: 14px; height: 14px; border-radius: 50%;
    background: var(--brand-red);
  }
  .card--front .brand { left: 344px; top: 128px; font-size: 26px; }
  .card--back .brand { left: 392px; top: 214px; font-size: 46px; gap: 16px; }
  .card--back .brand__dot { width: 24px; height: 24px; }

  .person { position: absolute; left: 48px; top: 250px; }
  .person__name { font-size: 21px; letter-spacing: 0.2px; }
  .person__title {
    display: flex; align-items: center; gap: 8px;
    margin-top: 4px; margin-left: 2px; font-size: 16px;
  }
  .person__title-rule { width: 142px; height: 2px; background: var(--ink); }
  .about {
    position: absolute; left: 48px; top: 340px;
    font-size: 17.5px; line-height: 27px;
  }
  .divider {
    position: absolute; left: 383px; top: 295px;
    width: 2px; height: 110px; background: var(--ink);
  }
  .contacts {
    position: absolute; left: 413px; top: 304px;
    list-style: none; font-size: 17.5px;
  }
  .contacts li {
    display: flex; align-items: center; gap: 14px;
    height: 30px;
  }
  .contacts svg { width: 16px; height: 16px; flex: none; }

  .tagline {
    position: absolute; left: 0; right: 0; top: 382px;
    text-align: center; font-size: 28px; letter-spacing: 0.5px;
  }
</style>
</head>
<body>
  <div class="sheet-frame"></div>

  <section class="card card--front">
    <div class="brand"><span class="brand__dot"></span>RESCUE READY ACADEMY</div>

    <div class="person">
      <p class="person__name">Your Name John Doe</p>
      <p class="person__title">Your title <span class="person__title-rule"></span></p>
    </div>
    <p class="about">We teach EMT's and we<br>are based out of Virginia.</p>

    <div class="divider"></div>

    <ul class="contacts">
      <li>
        <svg viewBox="0 0 16 16" aria-hidden="true"><rect x="3.5" y="1" width="9" height="14" rx="1.5" fill="none" stroke="#fff" stroke-width="1.6"/><rect x="5.5" y="3.5" width="5" height="6" fill="#fff"/><circle cx="8" cy="12.3" r="1" fill="#fff"/></svg>
        555.014.2287
      </li>
      <li>
        <svg viewBox="0 0 16 16" aria-hidden="true"><rect x="1.5" y="3.5" width="13" height="9" fill="#fff"/><path d="M1.5 3.5 L8 9 L14.5 3.5" fill="none" stroke="#222b35" stroke-width="1.4"/></svg>
        hello@rescueready.org
      </li>
      <li>
        <svg viewBox="0 0 16 16" aria-hidden="true"><g fill="none" stroke="#fff" stroke-width="1.8" stroke-linecap="round"><path d="M7 9.5 L4.5 12 a2 2 0 0 1 -2.8 -2.8 L4.5 6.5"/><path d="M9 6.5 L11.5 4 a2 2 0 0 1 2.8 2.8 L11.5 9.5"/><path d="M6 10 L10 6"/></g></svg>
        www.rescuereadyacademy.com
      </li>
    </ul>
  </section>

  <section class="card card--back">
    <div class="brand"><span class="brand__dot"></span>RESCUE READY ACADEMY</div>
    <p class="tagline">We Help You, Help Others</p>
  </section>
</body>
</html>
```